Brivet Networks, Inc. Website redesign

Revamp the website, it is old and outdated. www.brivetnetworksinc.com

Target Market(s)

Information Technology Consulting and Staffing

Coding

Coded - Design and coding required

Number of Pages Required

5+ page

Colors

Designer to choose colors to be used in the design.

Requirements
Must have
• Outlined text boxes just like from the Hollis.us site. A clean look

```html
<!DOCTYPE html>
<html lang="en">
<head>
<meta charset="utf-8">
<title>Brivet Networks, Inc.</title>
<link href="https://fonts.googleapis.com/css2?family=Lato:ital,wght@0,400;0,700;1,400&family=Rajdhani:wght@500;600;700&display=swap" rel="stylesheet">
<style>
:root{
  --red:#a51c30;
  --dark:#231f20;
  --ink:#2b2b2b;
  --muted:#555;
  --page:#f6f6f6;
  --white:#fff;
  --line:#cfcfcf;
}
*{margin:0;padding:0;box-sizing:border-box}
html,body{width:1200px;height:3213px;overflow:hidden}
body{font-family:'Lato',sans-serif;color:var(--ink);background:var(--page);position:relative}
.abs{position:absolute}
.heading{font-family:'Rajdhani',sans-serif;font-weight:500;font-size:37px;color:#333;text-align:center;width:100%}
.btn{display:flex;align-items:center;justify-content:center;background:var(--red);color:var(--white);font-size:14px;border-radius:18px;height:36px;width:145px}
/* header */
.site-header{left:0;top:0;width:1200px;height:102px;background:var(--white)}
.brand{left:80px;top:28px;font-family:'Lato',sans-serif;font-weight:700;font-size:38px;letter-spacing:2px;color:var(--dark);display:flex;align-items:center;gap:10px}
.brand .mark{width:26px;height:26px;background:var(--red)}
.call{left:812px;top:36px;display:flex;gap:8px;align-items:center}
.call .ic{width:28px;height:28px;border-radius:50%;background:var(--red);display:flex;align-items:center;justify-content:center}
.call small{display:block;color:var(--red);font-size:12px}
.call b{font-weight:400;font-size:13px}
.quote{left:975px;top:35px;width:145px}
.nav{left:0;top:102px;width:1200px;height:37px;background:var(--red);display:flex;padding-left:80px}
.nav a{color:var(--white);text-decoration:none;font-size:14px;width:155px;display:flex;align-items:center;justify-content:center;border-right:1px solid rgba(255,255,255,.25);margin:6px 0}
.nav a.active{background:#111;margin:0;width:137px;border:none}
/* hero */
.hero{left:0;top:139px;width:1200px;height:451px;background:radial-gradient(ellipse at 50% 55%,#39b6e8 0%,#0b6aa6 30%,#06345f 65%,#041a33 100%)}
.hero h1{font-family:'Rajdhani',sans-serif;font-weight:600;font-size:37px;color:var(--white);text-align:center;position:absolute;top:156px;width:100%}
.hero p{position:absolute;top:203px;width:380px;left:410px;text-align:center;color:var(--white);font-size:12px;line-height:16px}
.hero .btn{position:absolute;left:531px;top:253px}
/* about */
.about-text{left:80px;top:724px;width:510px;font-size:13px;line-height:16.5px;color:#444}
.about-text h3{font-family:'Rajdhani',sans-serif;font-weight:600;font-size:21px;color:#333;line-height:20px}
.about-text p{margin-bottom:17px}
.photo{display:block}
/* services */
.card{background:var(--white);text-align:center}
.card .photo{height:148px}
.card h4{font-family:'Lato',sans-serif;font-weight:400;font-size:17px;letter-spacing:.3px;margin:13px 0 10px;color:#333}
.card p{font-size:13px;line-height:16px;color:#555;padding:0 12px}
.card svg{margin-top:14px}
/* strategy */
.strategy{left:0;top:1510px;width:1200px;height:457px;background:linear-gradient(120deg,#2a2628 0%,#1b1819 45%,#2d292b 70%,#141213 100%)}
.strategy-text{left:80px;top:80px;width:495px;color:var(--white);font-size:13px;line-height:16.5px}
.strategy-text h2{font-family:'Rajdhani',sans-serif;font-weight:600;font-size:35px;line-height:36px}
.strategy-text h3{font-family:'Rajdhani',sans-serif;font-weight:700;font-size:21px;margin:6px 0 2px}
.strategy-text p{margin-bottom:15px}
/* news */
.news{background:var(--white);padding:12px}
.news .photo{height:205px;position:relative}
.date{position:absolute;left:6px;bottom:7px;width:50px;height:45px;background:var(--red);color:var(--white);font-size:13px;line-height:16px;padding:6px 0 0 8px}
.news h5{font-weight:400;font-size:14px;margin:15px 6px 10px}
.news p{font-size:13px;line-height:16px;color:#666;margin:0 6px;letter-spacing:.6px}
.news a{display:block;margin:10px 6px 0;color:#444;font-size:14px}
/* contact */
.field{background:var(--white);border:1px solid var(--line);font-size:14px;color:#555;padding:12px 14px}
/* footer */
.footer{left:0;top:2853px;width:1200px;height:293px;background:var(--dark);color:var(--white)}
.footer .brand{color:var(--white);left:80px;top:55px}
.fcol h6{font-weight:400;font-size:14px;padding-bottom:12px;position:relative;margin-bottom:18px}
.fcol h6:after{content:"";position:absolute;left:0;bottom:0;width:38px;height:2px;background:var(--red)}
.fcol li{list-style:none;font-size:13px;letter-spacing:.8px;line-height:24px}
.fcol li:before{content:"• ";margin-right:6px}
.fcol .row{display:flex;gap:9px;font-size:13px;line-height:24px}
.email-box{background:var(--white);border-radius:18px;height:35px;color:#999;font-style:italic;font-size:13px;padding:10px 18px}
.bottom{left:0;top:3146px;width:1200px;height:67px;background:var(--white)}
.social{width:30px;height:30px;border-radius:50%;border:2px solid var(--red);display:inline-block;margin-left:8px}
.social.solid{background:var(--red)}
</style>
</head>
<body>

<header class="abs site-header">
  <div class="abs brand"><span>BRIVET</span><span class="mark"></span></div>
  <div class="abs call">
    <div class="ic"><svg width="14" height="14" viewBox="0 0 24 24"><path fill="#fff" d="M6.6 10.8a15 15 0 006.6 6.6l2.2-2.2c.3-.3.7-.4 1-.2 1.1.4 2.3.6 3.6.6.6 0 1 .4 1 1V20c0 .6-.4 1-1 1A17 17 0 013 4c0-.6.4-1 1-1h3.5c.6 0 1 .4 1 1 0 1.3.2 2.5.6 3.6.1.3 0 .7-.2 1z"/></svg></div>
    <div><small>Call Us Now</small><b>00 123 456 789</b></div>
  </div>
  <div class="abs btn quote">Get a Quote</div>
</header>
<nav class="abs nav">
  <a class="active">Home</a><a>About us</a><a>Services</a><a>Strategy</a><a>IT News</a><a style="border:none">Contact us</a>
</nav>

<section class="abs hero" role="img" aria-label="Photo of a server room aisle lit in blue">
  <h1>Mission Integrity Results</h1>
  <p>Lorem Ipsum simply dummy text of the printing &amp; typesetting next industry. Lorem Ipsum has been the industry's</p>
  <div class="btn">Read More</div>
</section>

<h2 class="abs heading" style="top:627px;left:6px">About us</h2>
<div class="abs about-text">
  <h3>Brivet Networks, Inc.</h3>
  <p>is an 8(a) innovative and rapidly growing full-service IT consulting firm. We provide our clients with cutting-edge technologies and the know-how to apply them to their individual business models.</p>
  <p>For over 20 + years, we have been providing reliable IT solutions to businesses in the Washington, DC Metro area and beyond. Our comprehensive services provide clients with unique technology solutions that are customized to meet the specific demands of their business.</p>
  <p>Look to our experts for strategic IT guidance, management and services that allows you to take your mind off technology and concentrate on your core area of business. Brivet Networks, Inc. provides cost-efficient solutions that simply make good sense.</p>
  <div class="btn" style="margin-top:12px">Read More</div>
</div>
<div class="abs photo" style="left:625px;top:698px;width:495px;height:330px;background:linear-gradient(135deg,#b9a27a,#4f7fa3 45%,#d8d2c8)" role="img" aria-label="Photo of a laptop on a wooden table beside a coffee cup"></div>

<h2 class="abs heading" style="top:1080px;left:-4px">Our Service</h2>
<div class="abs card" style="left:80px;top:1156px;width:244px;height:291px">
  <div class="photo" style="background:linear-gradient(135deg,#2e6fb8,#dfe8f2)" role="img" aria-label="Photo of a hand on a tablet showing charts"></div>
  <h4>Hardware / Software Sales</h4>
  <p>Lorem Ipsum simply an dummy text printing &amp; typesetting next industry has been the industry's</p>
  <svg width="20" height="20" viewBox="0 0 20 20"><circle cx="10" cy="10" r="8.5" fill="none" stroke="#333" stroke-width="1.4"/><path d="M8.5 6l4 4-4 4" fill="none" stroke="#333" stroke-width="1.4"/></svg>
</div>
<div class="abs card" style="left:345px;top:1156px;width:244px;height:291px">
  <div class="photo" style="background:linear-gradient(135deg,#1d2b3d,#5c87b0)" role="img" aria-label="Photo of two professionals with a laptop"></div>
  <h4>Professional Services</h4>
  <p>Lorem Ipsum simply an dummy text printing &amp; typesetting next industry has been the industry's</p>
  <svg width="20" height="20" viewBox="0 0 20 20"><circle cx="10" cy="10" r="8.5" fill="none" stroke="#333" stroke-width="1.4"/><path d="M8.5 6l4 4-4 4" fill="none" stroke="#333" stroke-width="1.4"/></svg>
</div>
<div class="abs card" style="left:610px;top:1156px;width:244px;height:291px">
  <div class="photo" style="background:linear-gradient(135deg,#1f3350,#2f7fd0)" role="img" aria-label="Photo of a businessman touching a glowing world map"></div>
  <h4>Technology Assessment</h4>
  <p>Lorem Ipsum simply an dummy text printing &amp; typesetting next industry has been the industry's</p>
  <svg width="20" height="20" viewBox="0 0 20 20"><circle cx="10" cy="10" r="8.5" fill="none" stroke="#333" stroke-width="1.4"/><path d="M8.5 6l4 4-4 4" fill="none" stroke="#333" stroke-width="1.4"/></svg>
</div>
<div class="abs card" style="left:875px;top:1156px;width:245px;height:291px">
  <div class="photo" style="background:linear-gradient(135deg,#24344d,#e4e6ea 60%,#c9433b)" role="img" aria-label="Photo of consultants reviewing documents at a desk"></div>
  <h4>Technology Consulting</h4>
  <p>Lorem Ipsum simply an dummy text printing &amp; typesetting next industry has been the industry's</p>
  <svg width="20" height="20" viewBox="0 0 20 20"><circle cx="10" cy="10" r="8.5" fill="none" stroke="#333" stroke-width="1.4"/><path d="M8.5 6l4 4-4 4" fill="none" stroke="#333" stroke-width="1.4"/></svg>
</div>

<section class="abs strategy">
  <div class="abs strategy-text">
    <h2>Our Strategy</h2>
    <h3>Your Path to Success</h3>
    <p>Civilian and Federal agencies are facing increased demands driven by the changing economic environment and shifts in the way products and services are sold and delivered. These factors have created an imperative to leverage new and innovative technology solution architectures like cloud computing to help reduce cost and deliver profit-driving IT capabilities faster than ever before.</p>
    <p>Savvy businesses understand that technology investments cannot be made solely to enable internal and external operations; technology is now, more than ever, a critical component to retaining and winning customers as well as staying ahead of the competition. Leadership have the opportunity to introduce application,</p>
    <div class="btn" style="margin-top:17px">Read More</div>
  </div>
  <div class="abs photo" style="left:625px;top:63px;width:495px;height:330px;background:linear-gradient(135deg,#1e2a3a,#c9ced6 55%,#eef0f2)" role="img" aria-label="Photo of a team reviewing reports and a tablet"></div>
</section>

<h2 class="abs heading" style="top:2007px;left:3px">Latest News</h2>
<div class="abs news" style="left:80px;top:2078px;width:331px;height:348px">
  <div class="photo" style="background:linear-gradient(135deg,#1b2f4a,#2fa6de 55%,#0e2a44)" role="img" aria-label="Photo of hands holding a tablet with a security graphic"><div class="date">03<br>Sep</div></div>
  <h5>What is Lorem Ipsum?</h5>
  <p>Lorem Ipsum is simply dummy &nbsp;the printing and typesetting industry. Lorem Ipsum has been the standard dummy.</p>
  <a>Read More</a>
</div>
<div class="abs news" style="left:433px;top:2078px;width:331px;height:348px">
  <div class="photo" style="background:linear-gradient(135deg,#1a2230,#4b6d92 55%,#1d2a3a)" role="img" aria-label="Photo of two engineers in a server room"><div class="date">03<br>Sep</div></div>
  <h5>What is Lorem Ipsum?</h5>
  <p>Lorem Ipsum is simply dummy &nbsp;the printing and typesetting industry. Lorem Ipsum has been the standard dummy.</p>
  <a>Read More</a>
</div>
<div class="abs news" style="left:787px;top:2078px;width:333px;height:348px">
  <div class="photo" style="background:linear-gradient(135deg,#15202e,#3b5878 55%,#101923)" role="img" aria-label="Photo of a tablet with cloud network icons"><div class="date">03<br>Sep</div></div>
  <h5>What is Lorem Ipsum?</h5>
  <p>Lorem Ipsum is simply dummy &nbsp;the printing and typesetting industry. Lorem Ipsum has been the standard dummy.</p>
  <a>Read More</a>
</div>
<div class="abs btn" style="left:530px;top:2457px">View More</div>

<h2 class="abs heading" style="top:2524px;left:0">Quick Contact</h2>
<div class="abs field" style="left:276px;top:2589px;width:318px;height:43px">Name*</div>
<div class="abs field" style="left:276px;top:2645px;width:318px;height:43px">Phone*</div>
<div class="abs field" style="left:276px;top:2702px;width:318px;height:43px">Email*</div>
<div class="abs field" style="left:606px;top:2589px;width:316px;height:156px;padding-top:10px">Message</div>
<div class="abs btn" style="left:530px;top:2766px">Send</div>

<footer class="abs footer">
  <div class="abs brand"><span>BRIVET</span><span class="mark"></span></div>
  <p class="abs" style="left:80px;top:132px;width:270px;font-size:13px;line-height:16.5px">Lorem Ipsum is simply dummy text of the printing and typesetting industry industries Ipsum has been the industry's standard and dummy text ever since the 1500s,</p>
  <p class="abs" style="left:80px;top:222px;font-size:13px">Read More.. <svg width="14" height="14" viewBox="0 0 20 20" style="vertical-align:-2px"><circle cx="10" cy="10" r="8.5" fill="none" stroke="#fff" stroke-width="1.6"/><path d="M8.5 6l4 4-4 4" fill="none" stroke="#fff" stroke-width="1.6"/></svg></p>
  <div class="abs fcol" style="left:425px;top:55px">
    <h6>Quick Link</h6>
    <ul><li>Home</li><li>About us</li><li>Services</li><li>Strategy</li><li>IT News</li><li>Contact us</li></ul>
  </div>
  <div class="abs fcol" style="left:599px;top:55px;width:220px">
    <h6>Quick Contact</h6>
    <div class="row"><svg width="14" height="16" viewBox="0 0 14 16" style="margin-top:4px"><path d="M7 1a5 5 0 015 5c0 4-5 9-5 9S2 10 2 6a5 5 0 015-5z" fill="none" stroke="#fff"/><circle cx="7" cy="6" r="1.8" fill="none" stroke="#fff"/></svg><span>48 Alder Row, Westbrook,<br>New York 12345,<br>United States</span></div>
    <div class="row"><svg width="14" height="14" viewBox="0 0 14 14" style="margin-top:5px"><rect x="1.5" y="4" width="11" height="8" rx="1" fill="none" stroke="#fff"/><path d="M2 4c0-2 10-2 10 0" fill="none" stroke="#fff"/></svg><span>(00) 123 456 789</span></div>
    <div class="row"><svg width="14" height="12" viewBox="0 0 14 12" style="margin-top:6px"><rect x="1" y="1" width="12" height="9" fill="none" stroke="#fff"/><path d="M1 1l6 5 6-5" fill="none" stroke="#fff"/></svg><span>info@brivetnetworksinc.com</span></div>
  </div>
  <div class="abs fcol" style="left:875px;top:55px;width:245px">
    <h6>Join Our Newletter</h6>
    <p style="font-size:13px;line-height:16px;margin-bottom:18px">Lorem Ipsum is simply dummy the printing and typesetting industry.</p>
    <div class="email-box">Email Here</div>
    <div class="btn" style="width:245px;margin-top:10px">Subscribe</div>
  </div>
</footer>
<div class="abs bottom">
  <p class="abs" style="left:80px;top:26px;font-size:13px">Copyright © 2019 Brivet Networks Inc. All Right Reserved</p>
  <div class="abs" style="left:917px;top:18px"><span class="social solid"></span><span class="social"></span><span class="social"></span><span class="social"></span><span class="social"></span></div>
</div>

</body>
</html>
```